Pipe Bursting Company Brochure

Need a tri-fold brochure on our company. We are a underground water replacement company that specializes in Trenchless replacement of water systems utilizing "Pipe Bursting" techniques and HDPE pipe materials that come with a 50 year warranty on material and labot.

```html
<!DOCTYPE html>
<html lang="en">
<head>
<meta charset="utf-8">
<title>HDLine Tri-fold Brochure</title>
<link rel="stylesheet" href="https://fonts.googleapis.com/css2?family=Montserrat:wght@400;500;600;700&family=Lato:wght@400;700&display=swap">
<style>
:root{
  --blue:#1b5fd1;
  --ink:#2d2d2d;
  --text:#3a3a3a;
  --gray:#4a4a4a;
  --bg:#a9a9a9;
  --paper:#ffffff;
  --gold:#c9a23a;
  --photo-earth:#b08a5a;
  --photo-site:#8a6f4d;
}
*{margin:0;padding:0;box-sizing:border-box}
html,body{width:1200px;height:2392px;overflow:hidden;background:var(--bg)}
body{position:relative;font-family:"Lato",sans-serif;color:var(--text)}
.spread{position:absolute;left:40px;width:1120px;height:798px;background:var(--paper);overflow:hidden;box-shadow:0 6px 18px rgba(0,0,0,.25)}
.spread--outside{top:348px}
.spread--inside{top:1246px}
.spread svg.shapes{position:absolute;left:0;top:0}
.block{position:absolute}
.heading{font-family:"Montserrat",sans-serif;font-weight:600;color:var(--blue);font-size:17px;line-height:1.25;text-transform:uppercase}
.body{font-size:12px;line-height:1.3;text-align:justify;color:var(--text)}
.body p+p{margin-top:9px}
.brand{display:flex;align-items:center;gap:10px;font-family:"Montserrat",sans-serif;font-weight:700;color:var(--blue);font-size:50px;line-height:1}
.brand-dot{width:30px;height:30px;border-radius:50%;background:var(--blue)}
.tagline{font-family:"Montserrat",sans-serif;font-size:9px;letter-spacing:1.5px;color:var(--ink);text-transform:uppercase;margin-top:6px;text-align:center}
.contact{text-align:center;font-size:13.5px;color:var(--ink)}
.contact h3{font-family:"Montserrat",sans-serif;font-weight:500;font-size:19px;margin-bottom:26px}
.contact .icon{display:block;margin:0 auto 8px}
.contact p{margin-bottom:22px;line-height:1.6}
.title{text-align:center;font-family:"Montserrat",sans-serif;color:var(--ink);line-height:1.1}
.title .t1{font-size:29px;font-weight:400;letter-spacing:1px}
.title .t2{font-size:35px;font-weight:600;color:var(--blue)}
.title .t3{font-size:22px;font-weight:400}
.sub{font-family:"Montserrat",sans-serif;font-size:11.5px;color:var(--blue);text-transform:uppercase;line-height:1.3;margin-top:2px}
.list{list-style:none;margin-top:16px}
.list li{position:relative;padding-left:22px;font-size:12.3px;line-height:1.3;margin-bottom:9px}
.list li svg{position:absolute;left:0;top:2px}
.services{display:grid;grid-template-columns:1fr 1fr;row-gap:22px;margin-top:18px;text-align:center}
.services span{display:block;font-family:"Montserrat",sans-serif;font-size:11.5px;color:var(--ink);margin-top:6px;text-transform:uppercase}
.note{font-size:12px;line-height:1.3;margin-top:14px}
</style>
</head>
<body>

<!-- Outside spread -->
<section class="spread spread--outside">
  <svg class="shapes" width="1120" height="798" viewBox="0 0 1120 798">
    <circle cx="248" cy="630" r="256" fill="var(--blue)"/>
    <circle cx="238" cy="644" r="248" fill="#fff"/>
    <circle cx="236" cy="648" r="240" fill="var(--photo-earth)" role="img" aria-label="Photo of a worker joining a large pipe in a dug trench"/>
    <circle cx="201" cy="402" r="64" fill="#262626" stroke="var(--gold)" stroke-width="8"/>
    <path d="M742 156 Q990 176 1120 70 L1120 110 Q990 200 742 160 Z" fill="var(--blue)"/>
    <path d="M990 0 Q1070 60 1120 60 L1120 0 Z" fill="#f1f1f1"/>
    <circle cx="940" cy="770" r="392" fill="var(--blue)"/>
    <circle cx="950" cy="772" r="384" fill="#fff"/>
    <circle cx="954" cy="774" r="378" fill="var(--photo-site)" role="img" aria-label="Photo of a worker in orange overalls fitting a blue flanged pipe valve"/>
    <path d="M1120 340 Q1060 344 1010 372 Q1080 360 1120 366 Z" fill="var(--gray)"/>
  </svg>

  <div class="block" style="left:46px;top:50px;width:310px">
    <h2 class="heading">We are providing<br>50 years warranty</h2>
    <div class="body" style="margin-top:6px">
      <p>Lorem Ipsum is simply dummy text of the printing and typesetting industry. Lorem Ipsum has been the industry's standard dummy text ever since the 1500s, when an unknown printer took a galley of type and scrambled it to make a type specimen book. It has survived not only five centuries, but also the leap into electronictype setting, unchanged. It was popularised in the 1960s with the release of Letraset sheets containing Lorem Ipsum passages, and more recently with desktop publishing software like Aldus PageMaker including versions of Lorem Ipsum.printer took a galley of type and scrambled it to make a type specimen book. It has survived not only five centuries, but also the leap into</p>
    </div>
  </div>

  <div class="block" style="left:373px;top:56px;width:373px">
    <div style="display:flex;flex-direction:column;align-items:center">
      <div class="brand" style="font-size:44px"><span class="brand-dot" style="width:26px;height:26px"></span>HDLine</div>
      <div class="tagline">No Dig No Worries</div>
    </div>
    <div class="contact" style="margin-top:40px">
      <h3>CONTACT US</h3>
      <svg class="icon" width="24" height="24" viewBox="0 0 24 24"><circle cx="12" cy="12" r="12" fill="var(--blue)"/><path d="M6 12.5 12 7l6 5.5h-2V17h-3v-3h-2v3H8v-4.5Z" fill="#fff"/></svg>
      <p style="font-size:12px">18 Harbor Lane 40217, Riverton, Greece</p>
      <svg class="icon" width="24" height="24" viewBox="0 0 24 24"><circle cx="12" cy="12" r="12" fill="var(--blue)"/><path d="M8.5 6.5c.6-.4 1.3-.3 1.6.3l1 1.9c.3.5.1 1.1-.3 1.4l-.8.6c.5 1.3 1.6 2.5 3 3.1l.6-.8c.3-.4.9-.6 1.4-.3l1.9 1c.6.3.7 1 .3 1.6-.8 1.1-2 1.6-3.3 1.1-3-1.1-5.3-3.4-6.3-6.4-.4-1.3 0-2.6 1.1-3.3Z" fill="#fff"/></svg>
      <p>+30-2105550142 (landline)<br>+30-6975550187 (mobile phone)</p>
      <svg class="icon" width="24" height="24" viewBox="0 0 24 24"><circle cx="12" cy="12" r="12" fill="var(--blue)"/><circle cx="12" cy="12" r="6" fill="none" stroke="#fff" stroke-width="1.4"/><path d="M6 12h12M12 6c-2.5 3-2.5 9 0 12M12 6c2.5 3 2.5 9 0 12" fill="none" stroke="#fff" stroke-width="1.2"/></svg>
      <p>www.hdlinepipe.com</p>
    </div>
  </div>

  <div class="block" style="left:800px;top:56px;width:300px">
    <div class="brand"><span class="brand-dot"></span>HDLine</div>
    <div class="tagline" style="text-align:left;margin-left:48px">No Dig No Worries</div>
  </div>
  <div class="block title" style="left:746px;top:226px;width:374px">
    <div class="t1">HIGH-DENSITY</div>
    <div class="t2">POLYETHYLENE</div>
    <div class="t3">WATER AND SEWER</div>
  </div>
</section>

<!-- Inside spread -->
<section class="spread spread--inside">
  <svg class="shapes" width="1120" height="798" viewBox="0 0 1120 798">
    <circle cx="790" cy="-40" r="385" fill="var(--gray)"/>
    <circle cx="858" cy="8" r="382" fill="var(--blue)"/>
    <circle cx="854" cy="0" r="375" fill="#fff"/>
    <circle cx="854" cy="-4" r="368" fill="var(--photo-earth)" role="img" aria-label="Photo of a worker standing over blue HDPE pipe joints and valves in an excavation"/>
    <circle cx="132" cy="660" r="252" fill="var(--blue)"/>
    <circle cx="126" cy="668" r="244" fill="#fff"/>
    <circle cx="125" cy="672" r="238" fill="var(--photo-earth)" role="img" aria-label="Photo of long black polyethylene pipes laid through a sandy trench"/>
  </svg>

  <div class="block" style="left:46px;top:46px;width:310px">
    <h2 class="heading">Who we are?</h2>
    <div class="body" style="margin-top:8px">
      <p>Lorem Ipsum is simply dummy text of the printing and typesetting industry. Lorem Ipsum has been the industry's standard dummy text.</p>
      <p>ever since the 1500s, when an unknown printer took a galley of type and scrambled it to make a type specimen book. It has survived not only five centuries,but also the leap into electronictype setting, unchanged. It was popularised in the 1960s with the release of Letraset sheets containing Lorem Ipsum passages,</p>
      <p>and more recently with desktop publishing software like Aldus PageMaker including versions of Lorem Ipsum.printer took a galley of type and scrambled it to make a type specimen book. It has survived not only five centuries, but also the leap into1960s with the release of Letraset sheets containing</p>
      <p>Lorem Ipsum passages, and more recently with desktop publishing software like Aldus PageMaker including versions of Lorem Ipsum.</p>
    </div>
  </div>

  <div class="block" style="left:410px;top:308px;width:326px">
    <h2 class="heading">Product description</h2>
    <div class="sub">High-density poly ethylene<br>water and sewer pipe</div>
    <ul class="list">
      <li><svg width="13" height="13" viewBox="0 0 13 13"><circle cx="6.5" cy="6.5" r="5.7" fill="none" stroke="var(--blue)" stroke-width="1.3"/><path d="M4 6.6l1.8 1.8L9 5" fill="none" stroke="var(--blue)" stroke-width="1.3"/></svg>Lorem Ipsum is simply dummy text of the printing and typesetting industry. Lorem Ipsum has been the industry's standard dummy text ever since the 1500s.</li>
      <li><svg width="13" height="13" viewBox="0 0 13 13"><circle cx="6.5" cy="6.5" r="5.7" fill="none" stroke="var(--blue)" stroke-width="1.3"/><path d="M4 6.6l1.8 1.8L9 5" fill="none" stroke="var(--blue)" stroke-width="1.3"/></svg>Lorem Ipsum is simply dummy text of the printing and typesetting industry.</li>
      <li><svg width="13" height="13" viewBox="0 0 13 13"><circle cx="6.5" cy="6.5" r="5.7" fill="none" stroke="var(--blue)" stroke-width="1.3"/><path d="M4 6.6l1.8 1.8L9 5" fill="none" stroke="var(--blue)" stroke-width="1.3"/></svg>Lorem Ipsum is simply dummy text of the printing and typesetting industry. Lorem Ipsum has been the industry's standard.</li>
      <li><svg width="13" height="13" viewBox="0 0 13 13"><circle cx="6.5" cy="6.5" r="5.7" fill="none" stroke="var(--blue)" stroke-width="1.3"/><path d="M4 6.6l1.8 1.8L9 5" fill="none" stroke="var(--blue)" stroke-width="1.3"/></svg>Lorem Ipsum is simply dummy text of the printing and typesetting industry. Lorem Ipsum has been the industry's standard dummy text ever since the 1500s. Lorem Ipsum is simply dummy text of the printing and typesetting industry.</li>
      <li><svg width="13" height="13" viewBox="0 0 13 13"><circle cx="6.5" cy="6.5" r="5.7" fill="none" stroke="var(--blue)" stroke-width="1.3"/><path d="M4 6.6l1.8 1.8L9 5" fill="none" stroke="var(--blue)" stroke-width="1.3"/></svg>Lorem Ipsum is simply dummy text of the printing and typesetting industry. Lorem Ipsum has been the industry's standard dummy text ever since.</li>
      <li><svg width="13" height="13" viewBox="0 0 13 13"><circle cx="6.5" cy="6.5" r="5.7" fill="none" stroke="var(--blue)" stroke-width="1.3"/><path d="M4 6.6l1.8 1.8L9 5" fill="none" stroke="var(--blue)" stroke-width="1.3"/></svg>Lorem Ipsum is simply dummy text of the printing and typesetting industry. Lorem Ipsum has been the industry's standard dummy text ever since. Lorem Ipsum is simply dummy text of the printing and typesetting industry. Lorem Ipsum has been the industry's standard dummy text ever since.</li>
    </ul>
  </div>

  <div class="block" style="left:777px;top:440px;width:305px">
    <h2 class="heading">What we do?</h2>
    <p class="body" style="margin-top:6px;text-align:left">Lorem Ipsum is simply dummy text of the printing and typesetting industry. Lorem Ipsum has been the industry's standard dummy text ever since the 1500s, Lorem Ipsum is simply dummy text of the printing and typesetting industry.</p>
    <div class="services">
      <div>
        <svg width="40" height="40" viewBox="0 0 40 40" fill="none" stroke="var(--blue)" stroke-width="2"><path d="M26 6a8 8 0 0 0-9 10L7 26a3 3 0 0 0 4 4l10-10a8 8 0 0 0 10-9l-5 5-4-1-1-4Z"/></svg>
        <span>Repair</span>
      </div>
      <div>
        <svg width="40" height="40" viewBox="0 0 40 40" fill="none" stroke="var(--blue)" stroke-width="2"><circle cx="20" cy="20" r="6"/><path d="M20 5v5M20 30v5M5 20h5M30 20h5M9.4 9.4l3.5 3.5M27.1 27.1l3.5 3.5M9.4 30.6l3.5-3.5M27.1 12.9l3.5-3.5"/><circle cx="20" cy="20" r="11"/></svg>
        <span>Maintenance</span>
      </div>
      <div>
        <svg width="40" height="40" viewBox="0 0 40 40" fill="none" stroke="var(--blue)" stroke-width="2"><rect x="8" y="12" width="20" height="22"/><path d="M8 6h20M8 4v4M28 4v4M34 12v22M32 12h4M32 34h4"/></svg>
        <span>Dimensions</span>
      </div>
      <div>
        <svg width="40" height="40" viewBox="0 0 40 40" fill="none" stroke="var(--blue)" stroke-width="2"><rect x="6" y="6" width="28" height="28"/><path d="M12 28l2-6 14-14 4 4-14 14Z"/></svg>
        <span>Design</span>
      </div>
    </div>
    <p class="note">Polyethylene Water and Sewer Pipe for Municipal &amp; Industrial Applications</p>
  </div>
</section>

</body>
</html>
```